Bottlesuprises meets Kidshelp

Hello,

at first, please excuse my not percfect english, i'am from germany! :)

I have coded a .php-based website, this website is about mixing several things like chocolate, wine gums or little toys together and send them in a "tube" to the buyer adress or to a adress the buyer chose to suprise somebody.

A part of the revenue of every sold "tube", i want to give to german charity.

Please check uploaded pictures:

1.jpg: on this picture you see the mainsite. on the left side you see the "tube". This "tube" will be filled with the different things which will be chosed by user. Below the "tube" you will see the price and the quantity of fillable space in the "tube" in gramms. The user can chose "L", "XL" and "XXL", with this chose the user specific the high of the tube. On the right side you see the main menu, the user can now chose the different category, beginning from the top: gift wrap, chocolate, miscellaneous, the billing adress, the delivery adress and at last the order button.

around are little buttons like "tube", "how it works", "about us" etc.

2.jpg: here you see the "tubes", this "tubes" filled with chocolate or something else will be sended to user. You can see that the mainsite is in the middle window, if you click on a button, the window in the middle will change

3.jpg: here you can see the window if the user chose "chocolate" to pick some several chocolate to fill in the "tube"

To be honest iam still not sure in which direction i want to go, i like selfdrawed icons, modern look, but i think pictures for exampleof chocolate are also really cool! i think i want to have a modern-drawed-lovely-design with the charity-think (remember i will spent money for kids from the revenue of each sold "tube")!

I coded this website with .php, the outlines and grafics are .css based! i like the positions of each window and button, but of course i can change every width and hight of every field you see and of course i can move them or add new one.

Target Market(s)

people who want to spent money with buying something

Requirements
Must have
• - a logo, the website is called "plumvessel.de" (perhaps with a "tube" within)
- a painted or 3d-designed "tube" (filled with 1 thing to 100%, filled with 2 things each 50%, filled with 3 things each 33%, filled with 4 things each 25%, filled with 5 things each 20%) the user can chose up to 5 different things to fill in the "tube", if he chose for example 2 things, the "tube" on the left change to a tube filled with 2 things
- 4 different gift wrap layers (standard, christmas theme, birthday theme, neutral theme, eastern theme) this layer will be layed over the "tube" on the left if user chose one of them
- the right menue (6 "buttons" or pictures)
- perhaps a background for each category: gift wrap, chocolate, miscellaneous, billing adress, delivery adress order button.
- main background

```html
<!DOCTYPE html>
<html lang="de">
<head>
<meta charset="utf-8">
<title>Plumvessel</title>
<link href="https://fonts.googleapis.com/css2?family=PT+Sans:wght@400;700&family=Gelasio:wght@400;600&display=swap" rel="stylesheet">
<style>
:root{
  --page-bg:#e4e4e8;
  --frame:#d3d3d6;
  --panel:#fbfbfb;
  --band:#e8e4e5;
  --ink:#2e2e2e;
  --ink-soft:#555;
  --btn-top:#5a5a5a;
  --btn-bottom:#2c2c2c;
  --btn-text:#ffffff;
  --line:#3a3a3a;
  --light-btn-top:#ececec;
  --light-btn-bottom:#cfcfcf;
  --light-btn-text:#6a6a6a;
}
*{box-sizing:border-box;margin:0;padding:0}
html,body{width:1200px;height:672px;overflow:hidden}
body{background:radial-gradient(ellipse at 50% 40%,#f4f4f6 0%,var(--page-bg) 80%);font-family:"PT Sans",sans-serif;color:var(--ink);position:relative}
.frame{position:absolute;left:139px;top:0;width:920px;height:606px;background:var(--frame);border-radius:0 0 22px 22px}
.panel{position:absolute;left:150px;top:0;width:898px;height:595px;background:var(--panel);border-radius:0 0 18px 18px;box-shadow:0 2px 4px rgba(0,0,0,.08)}
.header-band{position:absolute;left:150px;top:47px;width:898px;height:46px;background:var(--band)}
.logo{position:absolute;left:186px;top:22px;font-family:"PT Sans",sans-serif;font-weight:700;font-size:46px;letter-spacing:-1.5px;color:#333}
.dark-btn{position:absolute;display:flex;align-items:center;justify-content:center;text-align:center;color:var(--btn-text);background:linear-gradient(var(--btn-top),var(--btn-bottom));border-radius:8px;box-shadow:0 2px 3px rgba(0,0,0,.25);font-size:13px;line-height:1.05}
.nav .dark-btn{top:117px;height:37px;width:197px;font-size:13px}
.card{position:absolute;background:#fff;border:1px solid var(--line);border-radius:9px;overflow:hidden}
.product{left:186px;top:165px;width:194px;height:331px}
.product-photo{position:absolute;left:72px;top:18px;width:50px;height:196px;border-radius:6px;background:linear-gradient(90deg,#1a1414,#4a3a36 45%,#1b1515)}
.price-row{position:absolute;left:0;width:100%;text-align:center;font-family:"Gelasio",serif;font-size:15px;color:#333}
.price-row.first{top:219px;height:37px;line-height:37px;border-top:1px solid #e6e6e6;border-bottom:1px solid #e6e6e6}
.price-row.second{top:256px;height:36px;line-height:36px}
.sizes{position:absolute;left:0;bottom:0;width:100%;height:38px;display:flex;background:linear-gradient(var(--btn-top),var(--btn-bottom))}
.sizes span{flex:1;color:#fff;font-size:15px;display:flex;align-items:center;justify-content:center;border-right:1px solid #222}
.sizes span:last-child{border:none}
.welcome{left:396px;top:165px;width:406px;height:285px;text-align:center;padding:22px 18px}
.welcome h1{font-family:"Gelasio",serif;font-weight:600;font-size:21px;color:#3a3a3a;margin-bottom:12px}
.welcome p{font-size:10px;line-height:1.45;color:#444;margin-bottom:5px}
.donation-label{margin-top:16px;font-size:10px!important;margin-bottom:0!important}
.donation-sum{font-size:19px;font-weight:700;color:#333;margin-bottom:8px}
.welcome .note{font-size:11px;margin-bottom:4px}
.sub .dark-btn{top:459px;height:37px}
.tile{position:absolute;left:815px;width:196px;height:58px;border-radius:8px;overflow:hidden;border:1px solid #ddd}
.tile-photo{position:absolute;inset:0}
.tile-label{position:absolute;left:0;bottom:0;width:100%;height:17px;background:rgba(60,60,60,.85);color:#fff;font-size:11.5px;text-align:center;line-height:17px}
.light-btn{position:absolute;left:815px;width:196px;height:37px;border-radius:6px;background:linear-gradient(var(--light-btn-top),var(--light-btn-bottom));border:1px solid #c4c4c4;display:flex;align-items:center;justify-content:space-between;padding:0 10px;font-family:"Gelasio",serif;font-size:17px;color:var(--light-btn-text)}
.light-btn svg{width:19px;height:19px}
.footer-band{position:absolute;left:150px;top:517px;width:898px;height:52px;background:var(--band)}
.social{position:absolute;top:533px;left:188px;display:flex;gap:9px}
.social span{width:21px;height:21px;border-radius:3px;background:#4a4a4a}
.footer-links{position:absolute;top:528px;right:193px;display:flex;height:30px;align-items:center;font-size:13px;color:#3e3e3e;text-transform:uppercase}
.footer-links a{color:inherit;text-decoration:none;padding:0 26px}
.footer-links a+a{border-left:1px solid #bbb}
.footer-links a:last-child{padding-right:0}
</style>
</head>
<body>
<div class="frame"></div>
<div class="panel"></div>
<div class="header-band"></div>
<div class="logo">Plumvessel</div>

<nav class="nav">
  <div class="dark-btn" style="left:186px">Die Tube</div>
  <div class="dark-btn" style="left:395px">Wie es Funktioniert</div>
  <div class="dark-btn" style="left:606px;font-size:12px">Das Kinderhilfe Netz</div>
  <div class="dark-btn" style="left:815px;font-size:12px">Was ist Plumvessel.de</div>
</nav>

<section class="card product">
  <div class="product-photo" role="img" aria-label="Dark chocolate tube product photo"></div>
  <div class="price-row first">ca.430 Gramm = € 16,90</div>
  <div class="price-row second">inkl, Mwst und Versand</div>
  <div class="sizes"><span>L</span><span>XL</span><span>XXL</span></div>
</section>

<section class="card welcome">
  <h1>Herzlich Willkommen</h1>
  <p>Lorem ipsum dolor sit amet, consectetur adipisicing elit, sed do eiusmod tempor incididunt ut labore et dolore magna aliqua. Duis aute irure dolor in reprehenderit in voluptate velit esse cillum dolore eu fugiat nulla pariatur.</p>
  <p>Ut enim ad minim veniam, quis nostrud exercitation, View more..</p>
  <p>Ut enim ad minim veniam, quis nostrud exercitation ullamco .Ut enim ad minim veniam, quis nostrud exercitation ullamco .</p>
  <p class="donation-label">BishiergeSpendunsemme</p>
  <div class="donation-sum">€2345,</div>
  <p class="note">aktueller Uberweisungsbeleg</p>
  <p class="note">Vilen Dank!</p>
</section>

<nav class="sub">
  <div class="dark-btn" style="left:396px;width:82px">TUBE</div>
  <div class="dark-btn" style="left:484px;width:84px">How it Works</div>
  <div class="dark-btn" style="left:574px;width:83px">About Us</div>
  <div class="dark-btn" style="left:664px;width:139px;font-size:12px">Ich akzeptiere die AGB<br>von plumvessel.de</div>
</nav>

<div class="tile" style="top:165px">
  <div class="tile-photo" role="img" aria-label="Red and white gift wrap photo" style="background:linear-gradient(135deg,#f3e6e6,#c8262a 55%,#e8d6d6)"></div>
  <div class="tile-label">Geschenkpapier</div>
</div>
<div class="tile" style="top:233px">
  <div class="tile-photo" role="img" aria-label="Wafer rolls, chocolate and kiwi photo" style="background:linear-gradient(90deg,#d9b27a,#8a9a3a 30%,#c79a5c 55%,#3b2418 85%)"></div>
  <div class="tile-label">Schokolade</div>
</div>
<div class="tile" style="top:300px">
  <div class="tile-photo" role="img" aria-label="Red strawberry dessert photo" style="background:linear-gradient(#fbeaea,#d63b3e 70%,#b8282b)"></div>
  <div class="tile-label">Diverses</div>
</div>

<div class="light-btn" style="top:367px">Billing Address<svg viewBox="0 0 20 20"><circle cx="10" cy="10" r="10" fill="#555"/><path d="M8 5.5l4.5 4.5L8 14.5" stroke="#fff" stroke-width="2.2" fill="none"/></svg></div>
<div class="light-btn" style="top:413px">Delivery Address<svg viewBox="0 0 20 20"><circle cx="10" cy="10" r="10" fill="#555"/><path d="M8 5.5l4.5 4.5L8 14.5" stroke="#fff" stroke-width="2.2" fill="none"/></svg></div>
<div class="light-btn" style="top:459px">ORDER NOW!<svg viewBox="0 0 20 20"><circle cx="10" cy="10" r="10" fill="#555"/><path d="M8 5.5l4.5 4.5L8 14.5" stroke="#fff" stroke-width="2.2" fill="none"/></svg></div>

<footer>
  <div class="footer-band"></div>
  <div class="social"><span></span><span></span><span></span><span></span></div>
  <div class="footer-links"><a>Allgemeiner Datenschutz</a><a>Impressum / AGB</a><a>Startseite</a></div>
</footer>
</body>
</html>
```